Swim School Certificates

We are looking to have some certificates designed for our Learn to Swim School. These will be handed out to our students when they complete each level. We will need different certificates for each level, however, we would like a consistent theme throughout, so each level may only have a slight variation. We are happy for you to just show us a couple of variations to begin with, so we can see how these would work. Then once we decide on the winning design, you can complete the rest.
The levels are:
Bubs 1
Bubs 2
Toddler 1
Toddler 2
Beginner 1
Beginner 2
Beginner 3
Stroke Development 1
Stroke Development 2
Advanced 1
Advanced 2
Squad
The Certificates should include:
Congratulations to:
(blank line for name)
You have completed (level name), Keep up the good work!!!
Signed: (blank line) Date: (blank line)
I've included a copy of our logo, and a copy of our governing bodies logo both of which should be included on the certificate.
I've also included some examples of certificates we like, to give you an idea of our style. We are happy for the bubs and toddler certificates to be more child focused, so they can included a kid friendly element to them, however this will need to reduce to a more simplistic design as the levels increase into beginner and stroke etc.
You can also look on our Facebook page to get an idea of what we do.
https://www.facebook.com/ripplecoveswimschool/?ref=bookmarks
We will also need editable source files upon completion as we may be looking to change the name of some classes in the future.
Please let us know if you need any of the files in other formats
Kind Regards
Maree

```html
<!DOCTYPE html>
<html lang="en">
<head>
<meta charset="utf-8">
<title>Ripple Cove Swim School – Level Certificates</title>
<link href="https://fonts.googleapis.com/css2?family=Nunito:wght@900&family=Source+Sans+3:wght@400;700&display=swap" rel="stylesheet">
<style>
  :root {
    --page: #f1ece2;
    --gold: #d8b93a;
    --gold-light: #f3df88;
    --paper: #ffffff;
    --ink: #111111;
    --red: #d5322b;
    --water-deep: #2f6fc4;
    --water-mid: #2b8fd0;
    --water-light: #33b3d8;
    --float-tone: #e9a94a;
    --logo-blue: #5fb8e8;
    --badge-blue: #1f8fd0;
  }
  * { box-sizing: border-box; margin: 0; padding: 0; }
  html, body { width: 1200px; height: 1200px; overflow: hidden; }
  body { background: var(--page); position: relative; font-family: "Source Sans 3", sans-serif; color: var(--ink); }

  .certificate {
    position: absolute;
    width: 538px; height: 418px;
    background: var(--paper);
    border: 6px solid var(--gold);
    box-shadow: inset 0 0 0 1px var(--gold-light), 0 2px 6px rgba(0,0,0,.18);
    overflow: hidden;
  }
  .certificate--toddler   { left: 38px;  top: 144px; }
  .certificate--beginner  { left: 622px; top: 144px; }
  .certificate--stroke    { left: 38px;  top: 645px; }
  .certificate--advanced  { left: 622px; top: 645px; }

  .water-panel { position: absolute; left: 0; top: 0; width: 200px; height: 406px; }

  .wording {
    position: absolute; left: 160px; width: 360px; top: 0;
    text-align: center;
  }
  .headline { position: absolute; left: 0; right: 0; top: 38px; font-family: "Nunito", sans-serif; font-weight: 900; font-size: 31px; letter-spacing: .5px; line-height: 1; }
  .student  { position: absolute; left: 0; right: 0; top: 82px; font-weight: 700; font-size: 22px; color: var(--red); line-height: 1; }
  .intro    { position: absolute; left: 0; right: 0; top: 133px; font-size: 17px; line-height: 1; }
  .level    { position: absolute; left: 0; right: 0; top: 162px; font-weight: 700; font-size: 18px; color: var(--red); letter-spacing: .5px; line-height: 1; }
  .encourage{ position: absolute; left: 0; right: 0; top: 190px; font-size: 17px; line-height: 1; }

  .sign-field { position: absolute; top: 250px; width: 114px; text-align: center; font-size: 12px; }
  .sign-field::after { content: ""; position: absolute; left: 0; right: 0; top: 43px; border-top: 1px solid #333; }
  .sign-field--signed { left: 219px; }
  .sign-field--date   { left: 357px; }

  .school-name {
    position: absolute; left: 262px; top: 326px; width: 92px;
    background: var(--logo-blue); color: #fff;
    font-size: 13px; font-weight: 700; line-height: 1.1; text-align: center;
    padding: 5px 4px;
  }
  .partner-badge {
    position: absolute; left: 364px; top: 318px; width: 58px; height: 58px;
    border-radius: 50%; border: 5px solid var(--badge-blue); background: #fff;
  }
</style>
</head>
<body>

<!-- Toddler 1 -->
<section class="certificate certificate--toddler">
  <svg class="water-panel" viewBox="0 0 200 406" role="img" aria-label="Pool lane with starfish, bubbles and an inflatable duck float">
    <defs>
      <linearGradient id="water-a" x1="0" y1="0" x2="1" y2="1">
        <stop offset="0" stop-color="var(--water-deep)"/><stop offset=".6" stop-color="var(--water-mid)"/><stop offset="1" stop-color="var(--water-light)"/>
      </linearGradient>
    </defs>
    <path d="M0 0 H128 C150 90 200 210 192 290 C186 350 170 385 160 406 H0 Z" fill="url(#water-a)"/>
    <path d="M70 0 C80 120 105 220 100 406" stroke="#fff" stroke-width="6" fill="none"/>
  </svg>
  <div class="wording">
    <h1 class="headline">CONGRATULATIONS</h1>
    <p class="student">Liam Okafor</p>
    <p class="intro">You have completed</p>
    <p class="level">TODDLER 1</p>
    <p class="encourage">Keep up the good work!!!</p>
  </div>
  <div class="sign-field sign-field--signed">Signed:</div>
  <div class="sign-field sign-field--date">Date:</div>
  <div class="school-name">Ripple Cove Swim School</div>
  <div class="partner-badge"></div>
</section>

<!-- Beginner 1 -->
<section class="certificate certificate--beginner">
  <svg class="water-panel" viewBox="0 0 200 406" role="img" aria-label="Pool lane with starfish, bubbles and a swim ring">
    <defs>
      <linearGradient id="water-b" x1="0" y1="0" x2="1" y2="1">
        <stop offset="0" stop-color="var(--water-deep)"/><stop offset=".6" stop-color="var(--water-mid)"/><stop offset="1" stop-color="var(--water-light)"/>
      </linearGradient>
    </defs>
    <path d="M0 0 H128 C150 90 200 210 192 290 C186 350 170 385 160 406 H0 Z" fill="url(#water-b)"/>
    <path d="M70 0 C80 120 105 220 100 406" stroke="#fff" stroke-width="6" fill="none"/>
  </svg>
  <div class="wording">
    <h1 class="headline">CONGRATULATIONS</h1>
    <p class="student">Liam Okafor</p>
    <p class="intro">You have completed</p>
    <p class="level">BEGINNER 1</p>
    <p class="encourage">Keep up the good work!!!</p>
  </div>
  <div class="sign-field sign-field--signed">Signed:</div>
  <div class="sign-field sign-field--date">Date:</div>
  <div class="school-name">Ripple Cove Swim School</div>
  <div class="partner-badge"></div>
</section>

<!-- Stroke Development 1 -->
<section class="certificate certificate--stroke">
  <svg class="water-panel" viewBox="0 0 200 406" role="img" aria-label="Pool lane with starfish, bubbles and a child swimming">
    <defs>
      <linearGradient id="water-c" x1="0" y1="0" x2="1" y2="1">
        <stop offset="0" stop-color="var(--water-deep)"/><stop offset=".6" stop-color="var(--water-mid)"/><stop offset="1" stop-color="var(--water-light)"/>
      </linearGradient>
    </defs>
    <path d="M0 0 H128 C150 90 200 210 192 290 C186 350 170 385 160 406 H0 Z" fill="url(#water-c)"/>
    <path d="M70 0 C80 120 105 220 100 406" stroke="#fff" stroke-width="6" fill="none"/>
  </svg>
  <div class="wording">
    <h1 class="headline">CONGRATULATIONS</h1>
    <p class="student">Liam Okafor</p>
    <p class="intro">You have completed</p>
    <p class="level">STROKE DEVELOPMENT 1</p>
    <p class="encourage">Keep up the good work!!!</p>
  </div>
  <div class="sign-field sign-field--signed">Signed:</div>
  <div class="sign-field sign-field--date">Date:</div>
  <div class="school-name">Ripple Cove Swim School</div>
  <div class="partner-badge"></div>
</section>

<!-- Advanced 1 -->
<section class="certificate certificate--advanced">
  <svg class="water-panel" viewBox="0 0 200 406" role="img" aria-label="Plain pool lane water">
    <defs>
      <linearGradient id="water-d" x1="0" y1="0" x2="1" y2="1">
        <stop offset="0" stop-color="var(--water-deep)"/><stop offset=".6" stop-color="var(--water-mid)"/><stop offset="1" stop-color="var(--water-light)"/>
      </linearGradient>
    </defs>
    <path d="M0 0 H80 C110 110 175 230 170 300 C166 350 150 385 138 406 H0 Z" fill="url(#water-d)"/>
    <path d="M68 0 C72 120 110 230 100 406" stroke="#fff" stroke-width="6" fill="none"/>
  </svg>
  <div class="wording">
    <h1 class="headline">CONGRATULATIONS</h1>
    <p class="student">Liam Okafor</p>
    <p class="intro">You have completed</p>
    <p class="level">ADVANCED 1</p>
    <p class="encourage">Keep up the good work!!!</p>
  </div>
  <div class="sign-field sign-field--signed">Signed:</div>
  <div class="sign-field sign-field--date">Date:</div>
  <div class="school-name">Ripple Cove Swim School</div>
  <div class="partner-badge"></div>
</section>

</body>
</html>
```